Personal wordpress site

I am documenting a few changes in my life and am looking for a designed wordpress theme to upload photos and short videos and a blurb tha tI can submit that will document the changes on a daily basis (for 12 weeks). It is a relatively straightforward site but one where I would like to track multiple projects in succession and have all the information.

Requirements
Must have
• I am looking for a dark, clean design.

```html
<!DOCTYPE html>
<html lang="en">
<head>
<meta charset="utf-8">
<title>My Personal Blog</title>
<link rel="stylesheet" href="https://fonts.googleapis.com/css2?family=Montserrat:wght@400;700&family=Arimo:wght@400&display=swap">
<style>
  :root {
    --page-bg: #181c20;
    --header-bg: #2b3039;
    --header-bg-dark: #23272e;
    --accent: #1bc5a0;
    --nav-ink: #1d3b35;
    --card-bg: #f9f9f9;
    --body-ink: #333638;
    --meta-ink: #b4b7b9;
    --footer-bg: #1a1e22;
    --bottom-bg: #14171a;
    --white: #ffffff;
    --icon: #4a5057;
  }
  * { box-sizing: border-box; }
  html, body { margin: 0; padding: 0; }
  body {
    width: 1200px; height: 2762px; overflow: hidden; position: relative;
    background: var(--page-bg);
    font-family: "Montserrat", sans-serif;
  }
  .site-header {
    position: absolute; left: 0; top: 0; width: 1200px; height: 224px;
    background: linear-gradient(180deg, var(--header-bg), var(--header-bg-dark));
    text-align: center;
  }
  .brand-mark {
    position: absolute; left: 584px; top: 44px; width: 32px; height: 32px;
    border-radius: 50%; background: var(--accent);
  }
  .site-title {
    position: absolute; left: 0; top: 100px; width: 1200px; margin: 0;
    color: var(--white); font-size: 31px; font-weight: 700;
  }
  .main-nav {
    position: absolute; left: 0; top: 224px; width: 1200px; height: 88px;
    background: var(--accent);
  }
  .main-nav a {
    position: absolute; top: 30px; font-size: 21px; color: var(--nav-ink);
    text-decoration: none; text-transform: uppercase; letter-spacing: 0.5px;
  }
  .main-nav a.current { color: var(--white); }

  .post-card {
    position: absolute; left: 148px; width: 898px; background: var(--card-bg);
    text-align: center;
  }
  .post-image {
    position: absolute; left: 0; top: 0; width: 898px; height: 300px;
    background: linear-gradient(180deg, #d9d8cc 0%, #c7c4b0 55%, #8d8a78 86%, #5a574a 100%);
  }
  .post-tag {
    position: absolute; left: 0; top: 28px; width: 132px; height: 58px;
    background: var(--accent); color: var(--white);
    font-family: "Arimo", sans-serif; font-size: 16px; line-height: 58px;
  }
  .post-meta {
    position: absolute; left: 0; width: 898px; color: var(--meta-ink);
    font-size: 13px; text-transform: uppercase; letter-spacing: 0.5px;
  }
  .post-title {
    position: absolute; left: 0; width: 898px; margin: 0; color: var(--accent);
    font-size: 41px; font-weight: 400; text-transform: uppercase; letter-spacing: 1px;
  }
  .post-excerpt {
    position: absolute; left: 44px; width: 816px; margin: 0; text-align: left;
    font-family: "Arimo", sans-serif; font-size: 19px; line-height: 34px; color: var(--body-ink);
  }
  .read-more {
    position: absolute; left: 0; width: 898px; color: var(--accent);
    font-size: 15px; text-transform: uppercase; letter-spacing: 0.8px; text-decoration: none;
  }
  .post-category {
    position: absolute; left: 44px; color: var(--meta-ink);
    font-size: 13px; text-transform: uppercase; letter-spacing: 0.5px;
  }

  .video-embed {
    position: absolute; left: 148px; top: 1160px; width: 898px; height: 540px;
    background: #101317;
  }
  .video-frame {
    position: absolute; left: 0; top: 0; width: 898px; height: 504px;
    background: radial-gradient(ellipse at 55% 40%, #b99b84 0%, #7a6a60 35%, #4b5766 70%, #2d3540 100%);
  }

  .pagination { position: absolute; left: 0; top: 2226px; width: 1200px; height: 40px; }
  .older-posts {
    position: absolute; left: 170px; top: 0; width: 126px; height: 38px;
    border: 2px solid var(--white); border-radius: 19px; color: var(--white);
    font-family: "Arimo", sans-serif; font-size: 13px; line-height: 34px; text-align: center;
    text-decoration: none;
  }
  .page-numbers { position: absolute; left: 584px; top: 8px; font-family: "Arimo", sans-serif; font-size: 15px; }
  .page-numbers .current { color: #3c4248; margin-right: 10px; }
  .page-numbers a { color: var(--white); text-decoration: none; }

  .site-footer { position: absolute; left: 0; top: 2300px; width: 1200px; height: 362px; background: var(--footer-bg); }
  .widget { position: absolute; top: 54px; width: 250px; }
  .widget h3 {
    margin: 0 0 18px; color: var(--white); font-size: 23px; font-weight: 400;
    text-transform: uppercase; line-height: 27px;
  }
  .widget ul { list-style: none; margin: 0; padding: 0; }
  .widget li {
    color: var(--white); font-size: 15px; line-height: 20px; margin-bottom: 16px;
  }
  .widget.comments li { margin-bottom: 16px; }

  .bottom-bar { position: absolute; left: 0; top: 2662px; width: 1200px; height: 100px; background: var(--bottom-bg); }
  .copyright { position: absolute; left: 40px; top: 66px; color: var(--white); font-size: 14px; }
  .social-links { position: absolute; left: 826px; top: 62px; width: 330px; height: 24px; }
</style>
</head>
<body>
  <header class="site-header">
    <span class="brand-mark"></span>
    <h1 class="site-title">My Personal Blog ...</h1>
  </header>

  <nav class="main-nav">
    <a class="current" href="#" style="left:250px">Home</a>
    <a href="#" style="left:354px">Menu 2</a>
    <a href="#" style="left:476px">Menu 3</a>
    <a href="#" style="left:598px">Menu 4</a>
    <a href="#" style="left:720px">Menu 5</a>
    <a href="#" style="left:842px">Contact</a>
  </nav>

  <article class="post-card" style="top:360px;height:742px">
    <div class="post-image" role="img" aria-label="Photo of a hazy beach with surfers in the distant waves"></div>
    <span class="post-tag">A beach</span>
    <div class="post-meta" style="top:364px">October 31, 2013 , &#9633; 2 , by Mr Lorne</div>
    <h2 class="post-title" style="top:380px">I went to the beach</h2>
    <p class="post-excerpt" style="top:440px">Lorem ipsum dolor sit amet, consectetur adipiscing elit. Fusce at risus at lacus laoreet mollis sed id elit. Integer bibendum lobortis velit, eleifend commodo dui facilisis nec. Aliquam mi sapien, ultrices a ultrices non, sodales ut diam. Fusce semper risus eu magna placerat pulvinar.</p>
    <a class="read-more" href="#" style="top:622px">Continue reading</a>
    <div class="post-category" style="top:674px">Saved as: Blog</div>
  </article>

  <section class="video-embed">
    <div class="video-frame" role="img" aria-label="Video still: close-up of a fine-tip pen touching paper, from a making-of film by Dana Reyes"></div>
  </section>

  <article class="post-card" style="top:1702px;height:468px">
    <div class="post-meta" style="top:94px">October 29, 2013 , &#9633; 0 , by Mr Lorne</div>
    <h2 class="post-title" style="top:110px">Some shots from the beach</h2>
    <p class="post-excerpt" style="top:170px">Lorem ipsum dolor sit amet, consectetur adipiscing elit. Fusce at risus at lacus laoreet mollis sed id elit. Integer bibendum lobortis velit, eleifend commodo dui facilisis nec. Aliquam mi sapien, ultrices a ultrices non, sodales ut diam. Fusce semper risus eu magna placerat pulvinar.</p>
    <a class="read-more" href="#" style="top:352px">Continue reading</a>
    <div class="post-category" style="top:404px">Saved as: Blog</div>
  </article>

  <nav class="pagination">
    <a class="older-posts" href="#">&larr; Older Posts</a>
    <div class="page-numbers"><span class="current">1</span><a href="#">2</a></div>
  </nav>

  <footer class="site-footer">
    <div class="widget" style="left:40px">
      <h3>Categories</h3>
      <ul><li>Audio</li><li>Blog</li><li>Chat</li><li>Quotes</li></ul>
    </div>
    <div class="widget" style="left:328px">
      <h3>Archives</h3>
      <ul><li>October 2013</li><li>September 2013</li></ul>
    </div>
    <div class="widget" style="left:616px">
      <h3>Recent Posts</h3>
      <ul><li>I went to the beach</li><li>Some video please</li><li>Great Quote</li><li>Some shots from the beach</li><li>Well he said that she said</li></ul>
    </div>
    <div class="widget comments" style="left:904px;width:240px">
      <h3>Recent<br>Comments</h3>
      <ul><li>Tess Oakley on I went to the beach</li><li>Carl Whitby on I went to the beach</li></ul>
    </div>
  </footer>

  <div class="bottom-bar">
    <div class="copyright">&copy; 2014</div>
    <svg class="social-links" viewBox="0 0 330 24" aria-label="Social links">
      <g fill="#4a5057">
        <circle cx="12" cy="12" r="11"/><circle cx="38" cy="12" r="11"/><circle cx="64" cy="12" r="11"/>
        <circle cx="90" cy="12" r="11"/><circle cx="116" cy="12" r="11"/><circle cx="142" cy="12" r="11"/>
        <circle cx="168" cy="12" r="11"/><circle cx="194" cy="12" r="11"/><circle cx="220" cy="12" r="11"/>
        <circle cx="246" cy="12" r="11"/><circle cx="272" cy="12" r="11"/><circle cx="298" cy="12" r="11"/>
        <circle cx="318" cy="12" r="0"/>
      </g>
    </svg>
  </div>
</body>
</html>
```